Zentrix Banner Grid Ads for Custom Software Company

We need some images for display on the Zentrix Banner Grid. Need a collection of them at different sizes.

This is for a custom software development company that specializes in small to medium size businesses.

PLEASE PLEASE PLEASE GET CREATIVE! That is the point! Something very typical and plain will not win!

Target Market(s)

Small and Medium sized businesses looking for custom software development services

Industry/Entity Type

Computer Software

Font styles to use
Serif
Sans Serif

Requirements
Must have
• Medium Rectangle (300×250)
• Large Rectangle (336×280)
• Leaderboard (728×90)
• Half Page (300×600)
• Large Mobile Banner (320×100)
• Needs to stand out, but not be obnoxious
• Needs to flow with the website design and colors (does not need to be the same colors, just needs to work together)
• Must have specific call to action (schedule appointment or read more are options, but feel free to make up more)
Nice to have
• Logo integration
• Adobe Illustrator files with artboards/exports for the different sizes
Should not have
• Should not have more than 20% text
• Don't steal from the slides on the website. We want "read more" to mean read more, not more of the same.

```html
<!DOCTYPE html>
<html lang="en">
<head>
<meta charset="utf-8">
<title>Novarel Display Ad Set</title>
<link rel="stylesheet" href="https://fonts.googleapis.com/css2?family=Bebas+Neue&family=Raleway:wght@500;600&display=swap">
<style>
  :root {
    --stage: #262626;
    --paper: #ffffff;
    --brand-blue: #1d4fa8;
    --accent-line: #22a9e1;
    --cta: #f7941d;
    --cta-edge: #e3800c;
    --cta-text: #1b1b1b;
    --headline: #ffffff;
    --photo-dark: #0a1f4a;
    --photo-mid: #0d5f8c;
    --photo-light: #1fc6dc;
    --photo-warm: #3a3442;
  }
  * { box-sizing: border-box; margin: 0; padding: 0; }
  html, body { width: 1200px; height: 800px; overflow: hidden; background: var(--stage); }
  .canvas { position: relative; width: 1200px; height: 800px; }

  .ad { position: absolute; background: var(--paper); overflow: hidden; box-shadow: 0 1px 3px rgba(0,0,0,.4); }
  .photo {
    position: absolute;
    background:
      radial-gradient(ellipse at 85% 10%, var(--photo-light) 0%, rgba(31,198,220,0) 55%),
      linear-gradient(100deg, var(--photo-warm) 0%, var(--photo-mid) 45%, var(--photo-dark) 100%);
  }
  .photo--tall {
    background:
      radial-gradient(ellipse at 50% 5%, var(--photo-light) 0%, rgba(31,198,220,0) 60%),
      linear-gradient(180deg, var(--photo-mid) 0%, #0c3c6e 55%, var(--photo-dark) 100%);
  }
  .rule { position: absolute; background: var(--accent-line); }

  .headline {
    position: absolute;
    font-family: "Bebas Neue", "Oswald", sans-serif;
    color: var(--headline);
    line-height: 1;
    letter-spacing: 0;
  }
  .headline--center { text-align: center; }
  .headline--right { text-align: right; }

  .brand { position: absolute; display: flex; align-items: center; gap: 6px; }
  .brand-mark { background: var(--brand-blue); flex: none; }
  .brand-name {
    font-family: "Raleway", "Helvetica Neue", sans-serif;
    font-weight: 500;
    color: var(--brand-blue);
    line-height: 1;
  }

  .cta {
    position: absolute;
    display: flex; align-items: center; justify-content: center;
    background: var(--cta);
    border: 1px solid var(--cta-edge);
    border-radius: 4px;
    font-family: "Raleway", "Helvetica Neue", sans-serif;
    font-weight: 600;
    color: var(--cta-text);
    white-space: nowrap;
  }
</style>
</head>
<body>
<main class="canvas">

  <!-- Half page 300x600 -->
  <section class="ad ad--half-page" style="left:189px; top:148px; width:240px; height:480px;">
    <div class="brand" style="left:44px; top:20px;">
      <span class="brand-mark" style="width:30px; height:30px;"></span>
      <span class="brand-name" style="font-size:28px;">Novarel</span>
    </div>
    <div class="rule" style="left:0; top:67px; width:240px; height:3px;"></div>
    <div class="photo photo--tall" role="img" aria-label="Blurred screen of program code glowing in teal and amber" style="left:0; top:70px; width:240px; height:353px;"></div>
    <h2 class="headline headline--center" style="left:0; top:88px; width:240px; font-size:35px;">Ambitious<br>Missions Need<br>Discruptive<br>Thinking</h2>
    <div class="rule" style="left:0; top:423px; width:240px; height:2px;"></div>
    <a class="cta" style="left:54px; top:437px; width:126px; height:30px; font-size:16px;">Learn More</a>
  </section>

  <!-- Large mobile banner 320x100 -->
  <section class="ad ad--mobile" style="left:477px; top:154px; width:257px; height:80px;">
    <div class="photo" role="img" aria-label="Blurred screen of program code glowing in teal and amber" style="left:0; top:0; width:157px; height:80px;"></div>
    <h2 class="headline" style="left:84px; top:8px; width:72px; font-size:15px; line-height:1.08;">Ambitious<br>Missions Need<br>Discruptive<br>Thinking</h2>
    <div class="rule" style="left:157px; top:0; width:2px; height:80px;"></div>
    <div class="brand" style="left:172px; top:20px; gap:4px;">
      <span class="brand-mark" style="width:16px; height:16px;"></span>
      <span class="brand-name" style="font-size:16px;">Novarel</span>
    </div>
    <a class="cta" style="left:165px; top:47px; width:86px; height:16px; font-size:11px; border-radius:2px;">Learn More</a>
  </section>

  <!-- Medium rectangle 300x250 -->
  <section class="ad ad--medium" style="left:477px; top:283px; width:270px; height:224px;">
    <div class="photo" role="img" aria-label="Blurred screen of program code glowing in teal and amber" style="left:0; top:0; width:270px; height:169px;"></div>
    <h2 class="headline headline--right" style="right:17px; top:31px; font-size:25px; line-height:1.18;">Ambitious<br>Missions Need<br>Discruptive<br>Thinking</h2>
    <div class="rule" style="left:0; top:169px; width:270px; height:3px;"></div>
    <a class="cta" style="left:13px; top:187px; width:98px; height:24px; font-size:13px;">Learn More</a>
    <div class="brand" style="left:135px; top:185px; gap:5px;">
      <span class="brand-mark" style="width:26px; height:26px;"></span>
      <span class="brand-name" style="font-size:23px;">Novarel</span>
    </div>
  </section>

  <!-- Large rectangle 336x280 -->
  <section class="ad ad--large" style="left:795px; top:307px; width:241px; height:200px;">
    <div class="photo" role="img" aria-label="Blurred screen of program code glowing in teal and amber" style="left:0; top:0; width:241px; height:150px;"></div>
    <h2 class="headline headline--right" style="right:15px; top:28px; font-size:22px; line-height:1.18;">Ambitious<br>Missions Need<br>Discruptive<br>Thinking</h2>
    <div class="rule" style="left:0; top:150px; width:241px; height:3px;"></div>
    <a class="cta" style="left:12px; top:166px; width:88px; height:21px; font-size:12px;">Learn More</a>
    <div class="brand" style="left:120px; top:164px; gap:5px;">
      <span class="brand-mark" style="width:24px; height:24px;"></span>
      <span class="brand-name" style="font-size:21px;">Novarel</span>
    </div>
  </section>

  <!-- Leaderboard 728x90 -->
  <section class="ad ad--leaderboard" style="left:477px; top:555px; width:584px; height:73px;">
    <div class="brand" style="left:14px; top:22px; gap:6px;">
      <span class="brand-mark" style="width:28px; height:28px;"></span>
      <span class="brand-name" style="font-size:24px;">Novarel</span>
    </div>
    <div class="rule" style="left:151px; top:0; width:2px; height:73px;"></div>
    <div class="photo" role="img" aria-label="Blurred screen of program code glowing in teal and amber" style="left:153px; top:0; width:307px; height:73px;"></div>
    <h2 class="headline headline--center" style="left:230px; top:13px; width:220px; font-size:24px; line-height:1;">Ambitious Missions Need<br>Discruptive Thinking</h2>
    <div class="rule" style="left:460px; top:0; width:2px; height:73px;"></div>
    <a class="cta" style="left:471px; top:24px; width:100px; height:24px; font-size:13px;">Learn More</a>
  </section>

</main>
</body>
</html>
```